Federal IT Consulting Company - Bridgemont Consulting Group

We're seeking a skilled web designer to create a modern, bold, and engaging WordPress website for Bridgemont Consulting Group, LLC. Our company specializes in federal IT consulting, and our name is a play on "Bridging Momentum." The website should reflect our expertise in the federal technology marketplace and position us as a trusted partner for clients navigating their IT journey.

contact: info@bridgemontgrp.com

Current Status

WordPress is already installed on our hosting account
We have an existing logo (may need modernization)

Design Requirements

Style:

Modern and visually striking design
Bold elements to convey confidence and expertise
Incorporate the concept of "bridging momentum" into the design

Features:

Modern UX sliders for dynamic content presentation
Eye-catching, high-quality images (stock photos to be sourced by the designer)
Responsive design for all devices

Color Scheme:

To be proposed by the designer, should align with our brand and convey trust and technological expertise

Logo:

Evaluate our current logo
Create a transparent background version if needed
Propose modernization if deemed necessary

Accessibility:

Ensure design elements are accessible to users with disabilities
Use high contrast ratios for text and background colors
Provide text alternatives for non-text content

Website Structure
Create the following pages, with the possibility of subpages:

Home
Services
About
Contact

Specific Page Requirements
Home Page

Striking hero section with a clear value proposition
Overview of our services
Client testimonials or trust indicators

Services Page

Detailed list of our IT consulting services
Clear explanation of how we help navigate the federal IT landscape

About Page

Company history and mission
Team highlights (if applicable)
Our approach to federal IT consulting

Contact Page

Contact form
Other contact methods (phone, email)

Technical Requirements

Fully responsive design
SEO best practices implemented
Fast loading times
Integration with necessary plugins (to be discussed)
Training on how to update and maintain the site
Full compliance with Web Content Accessibility Guidelines (WCAG) 2.1 Level AA
Adherence to Section 508 standards for federal website accessibility
Implementation of necessary features for ADA compliance
Updates

Designs look the same

Target Market(s)

US Federal Govt customers looking for IT support.

Industry/Entity Type

IT Consulting

Coding

Coded - Design and coding required

Colors
0054AA
0677BA
7BADD7
CADEEF
E8F1F8
0094D4
00A9DD
6FCCEA
C7EBF8
E9F6FB
00AB8E
00BBA5
67D7C9
C6EFE9
E9F9F6

```html
<!DOCTYPE html>
<html lang="en">
<head>
<meta charset="utf-8">
<title>Bridgemont Federal Services</title>
<link href="https://fonts.googleapis.com/css2?family=League+Spartan:wght@400;500;600;700;800&family=Outfit:wght@300;400;500;600&display=swap" rel="stylesheet">
<style>
:root{
  --blue:#00A9DD;
  --blue-deep:#0094D4;
  --blue-soft:#6FCCEA;
  --ink:#3b3b3b;
  --text:#222;
  --grey:#8a8a8a;
  --footer:#3a3a3a;
  --footer-bottom:#2c2c2c;
  --white:#fff;
}
*{margin:0;padding:0;box-sizing:border-box}
html,body{width:1200px;height:3254px;overflow:hidden;background:var(--white)}
body{position:relative;font-family:"Outfit",sans-serif;color:var(--text)}
.abs{position:absolute}
.heading{font-family:"League Spartan",sans-serif}

/* top bar */
.topbar{left:0;top:0;width:1200px;height:34px;background:var(--blue);color:var(--white);font-size:12px;font-weight:500}
.topbar span{position:absolute;top:9px;display:flex;align-items:center;gap:6px}

/* header */
.header{left:0;top:34px;width:1200px;height:89px;background:var(--white);border-bottom:1px solid #e6e6e6}
.brand{position:absolute;display:flex;align-items:center;gap:10px;font-family:"League Spartan",sans-serif;font-weight:700;color:var(--ink);letter-spacing:1px}
.brand i{display:block;border-radius:50%;background:var(--blue)}
.nav{position:absolute;top:38px;font-size:15px;color:#222;font-weight:400}
.nav.active{color:var(--blue)}
.nav.active::before{content:"";position:absolute;left:-16px;top:6px;width:6px;height:6px;background:var(--blue)}

/* hero */
.hero{left:0;top:123px;width:1200px;height:583px;background:linear-gradient(100deg,#0aa3dc 0%,#25b2e6 40%,#8fd6f2 55%,#cfd8de 70%,#a8aeb3 100%);overflow:hidden}
.hero-photo{position:absolute;left:540px;top:0;width:660px;height:583px;background:linear-gradient(90deg,rgba(60,190,235,0) 0%,rgba(200,205,210,.6) 25%,#7d838a 60%,#474b52 100%)}
.welcome{left:73px;top:215px;width:175px;height:33px;background:var(--white);border-radius:17px;font-size:19px;color:#222;text-align:center;line-height:34px}
.hero-title{left:74px;top:258px;font-size:92px;font-weight:800;color:var(--white);letter-spacing:1px;line-height:1}
.hero-sub{left:77px;top:337px;font-size:31px;font-weight:500;color:var(--white);letter-spacing:11.5px}
.hero-copy{left:78px;top:388px;width:430px;font-size:20px;line-height:39px;color:var(--white)}
.btn-dark{background:var(--ink);color:var(--white);border-radius:30px;display:flex;align-items:center;justify-content:center;gap:14px;font-weight:500}
.hero-btn{left:76px;top:480px;width:190px;height:58px;font-size:16px}

/* feature cards */
.card{top:632px;width:265px;height:330px;background:var(--white);box-shadow:0 2px 14px rgba(0,0,0,.12);text-align:center}
.card .ring{position:absolute;left:80px;top:35px;width:106px;height:106px;border:5px solid var(--blue);border-radius:50%;display:flex;align-items:center;justify-content:center}
.card h3{position:absolute;left:0;top:160px;width:100%;font-family:"League Spartan",sans-serif;font-size:21px;font-weight:600;color:#333}
.card p{position:absolute;left:20px;top:203px;width:225px;font-size:16px;line-height:23px;color:#444}
.card .more{position:absolute;left:0;top:265px;width:100%;display:flex;justify-content:center;align-items:center;gap:10px;color:var(--blue);font-size:16px;font-weight:500}

/* section headings */
.sec-title{font-family:"League Spartan",sans-serif;font-weight:700;color:var(--ink);font-size:58px;text-align:center;letter-spacing:-.5px}
.sec-title b{color:var(--blue);font-weight:700}

.svc-intro{left:170px;top:1212px;width:860px;text-align:center;font-size:15.5px;line-height:30px;color:#222}
.svc{top:1323px;width:250px;text-align:center}
.svc .ring{margin:0 auto;width:126px;height:126px;border:3px solid var(--blue);border-radius:50%;padding:6px}
.svc .ring div{width:100%;height:100%;border-radius:50%;background:var(--blue);display:flex;align-items:center;justify-content:center}
.svc h4{margin-top:22px;font-family:"League Spartan",sans-serif;font-size:23px;font-weight:600;color:#333}
.arrow{width:29px;height:29px;border-radius:50%;display:flex;align-items:center;justify-content:center;color:var(--white);font-size:16px;font-weight:700}
.arrow.prev{background:#9a9a9a}
.arrow.next{background:var(--blue)}

/* about */
.about-photo{left:84px;top:1638px;width:464px;height:464px;border-radius:50%;background:radial-gradient(circle at 55% 40%,#a9acaf 0%,#7b7e82 45%,#55585c 100%)}
.about-title{left:656px;top:1718px;font-family:"League Spartan",sans-serif;font-weight:700;font-size:42px;color:var(--ink)}
.about-copy{left:624px;top:1813px;width:492px;font-size:15.5px;line-height:30px;text-align:justify;color:#222}
.about-btn{left:624px;top:1997px;width:162px;height:44px;font-size:15px}

/* testimonials */
.quote-mark{left:158px;top:2385px;font-family:"League Spartan",sans-serif;font-size:150px;font-weight:800;color:var(--blue);line-height:1}
.testi-copy{left:253px;top:2398px;width:786px;font-size:15.5px;line-height:30px;color:#222;text-align:justify}
.avatar{left:492px;top:2573px;width:60px;height:60px;border-radius:50%;background:linear-gradient(160deg,#d9dcdf,#6e7277)}
.person{left:572px;top:2580px}
.person strong{display:block;font-family:"League Spartan",sans-serif;color:var(--blue);font-size:19px;font-weight:600}
.person span{font-size:13.5px;color:#222}
.dots{left:550px;top:2681px;display:flex;gap:13px;align-items:center}
.dots i{display:block;width:11px;height:11px;border-radius:50%;background:#cfcfcf}
.dots i.on{width:28px;height:7px;border-radius:4px;background:var(--blue)}

/* footer */
.footer{left:0;top:2857px;width:1200px;height:337px;background:var(--footer)}
.footer-bottom{left:0;top:3194px;width:1200px;height:60px;background:var(--footer-bottom);color:var(--white);font-size:13px;text-align:center;line-height:60px}
.newsletter{left:206px;top:2801px;width:789px;height:110px;background:var(--blue);border-radius:36px}
.newsletter h2{position:absolute;left:34px;top:34px;font-family:"League Spartan",sans-serif;font-size:33px;font-weight:500;color:var(--white)}
.field{position:absolute;left:410px;top:38px;width:350px;height:39px;background:var(--white);border-radius:20px;font-size:9px;color:#555;line-height:39px;padding-left:27px}
.field b{position:absolute;right:0;top:0;width:106px;height:39px;border-radius:20px;background:var(--ink);color:var(--white);font-size:14px;font-weight:500;text-align:center;line-height:39px;padding:0}
.f-title{font-family:"League Spartan",sans-serif;color:var(--white);font-size:16px;font-weight:500;display:flex;align-items:center;gap:6px}
.f-title i{display:block;width:10px;height:10px;border-radius:50%;background:var(--blue)}
.links{left:139px;top:3021px;list-style:none;color:var(--white);font-size:13.5px}
.links li{height:26.5px;display:flex;align-items:center;gap:12px}
.links li::before{content:"";width:9px;height:9px;border-radius:50%;background:var(--blue)}
.social{top:3122px;width:28px;height:28px;border:1.5px solid var(--blue);border-radius:50%}
.social::after{content:"";position:absolute;left:6px;top:6px;width:13px;height:13px;border-radius:50%;background:var(--white)}
.contact-item{left:868px;display:flex;gap:14px;color:var(--white);font-size:13.5px;line-height:17px;align-items:center}
.contact-item .ic{width:28px;height:28px;border:1.5px solid var(--blue);border-radius:50%;display:flex;align-items:center;justify-content:center}
</style>
</head>
<body>

<div class="abs topbar">
  <span style="left:800px">
    <svg width="14" height="14" viewBox="0 0 24 24" fill="none" stroke="#fff" stroke-width="2"><path d="M5 3h4l2 5-3 2a12 12 0 0 0 6 6l2-3 5 2v4a2 2 0 0 1-2 2A18 18 0 0 1 3 5a2 2 0 0 1 2-2z"/></svg>
    555-010-4827
  </span>
  <span style="left:947px">
    <svg width="15" height="12" viewBox="0 0 24 18" fill="none" stroke="#fff" stroke-width="2"><rect x="1" y="1" width="22" height="16" rx="2"/><path d="M1 2l11 8 11-8"/></svg>
    INFO@BRIDGEMONTGRP.COM
  </span>
</div>

<header class="abs header">
  <div class="brand" style="left:76px;top:26px;font-size:34px">
    <i style="width:34px;height:34px"></i>BRIDGEMONT
  </div>
  <span class="abs nav active" style="left:748px">HOME</span>
  <span class="abs nav" style="left:825px">SERVICES</span>
  <span class="abs nav" style="left:926px">ABOUT US</span>
  <span class="abs nav" style="left:1033px">CONTACT US</span>
</header>

<section class="abs hero">
  <div class="hero-photo" role="img" aria-label="Photo of three business consultants reviewing a document on a clipboard in a bright office"></div>
</section>
<div class="abs welcome">Welcome To</div>
<h1 class="abs heading hero-title">BRIDGEMONT</h1>
<div class="abs heading hero-sub">FEDERAL SERVICES</div>
<p class="abs hero-copy">Lorem ipsum dolor sit amet, consectetur adipis elit. Sed ut est sed nulla viverra fringilla.</p>
<div class="abs btn-dark hero-btn">CONTACT US
  <svg width="30" height="10" viewBox="0 0 30 10" fill="none" stroke="#fff" stroke-width="2"><path d="M0 5h28M23 1l5 4-5 4"/></svg>
</div>

<!-- feature cards -->
<div class="abs card" style="left:154px">
  <div class="ring">
    <svg width="44" height="48" viewBox="0 0 44 48" fill="#333"><path d="M22 10a11 11 0 0 0-7 19c2 2 3 4 3 6h8c0-2 1-4 3-6a11 11 0 0 0-7-19z"/><rect x="17" y="37" width="10" height="4" rx="1"/><rect x="18" y="42" width="8" height="3" rx="1"/><g stroke="#333" stroke-width="2.5" stroke-linecap="round"><path d="M22 1v4M6 8l3 3M38 8l-3 3M1 22h4M39 22h4"/></g></svg>
  </div>
  <h3>Innovative Solutions</h3>
  <p>Lorem ipsum dolor sit lorem amet, consectetur</p>
  <div class="more">READ MORE <svg width="30" height="10" viewBox="0 0 30 10" fill="none" stroke="#00A9DD" stroke-width="2"><path d="M0 5h28M23 1l5 4-5 4"/></svg></div>
</div>
<div class="abs card" style="left:467px">
  <div class="ring">
    <svg width="52" height="44" viewBox="0 0 52 44" fill="#333"><circle cx="26" cy="12" r="8"/><circle cx="11" cy="16" r="6"/><circle cx="41" cy="16" r="6"/><path d="M12 42c0-10 6-18 14-18s14 8 14 18z"/><path d="M1 38c0-8 4-14 10-14 2 0 3 0 4 1-3 4-5 8-5 13z"/><path d="M51 38c0-8-4-14-10-14-2 0-3 0-4 1 3 4 5 8 5 13z"/></svg>
  </div>
  <h3>Professional Team</h3>
  <p>Lorem ipsum dolor sit lorem amet, consectetur</p>
  <div class="more">READ MORE <svg width="30" height="10" viewBox="0 0 30 10" fill="none" stroke="#00A9DD" stroke-width="2"><path d="M0 5h28M23 1l5 4-5 4"/></svg></div>
</div>
<div class="abs card" style="left:780px">
  <div class="ring">
    <svg width="54" height="42" viewBox="0 0 54 42" fill="none" stroke="#333" stroke-width="3"><rect x="2" y="2" width="44" height="34" rx="2"/><path d="M10 12h22M10 19h18M10 26h14" stroke-linecap="round"/><circle cx="42" cy="28" r="7" fill="#fff"/><path d="M38 34l-2 7 6-3 6 3-2-7"/></svg>
  </div>
  <h3>24/7 Support</h3>
  <p>Lorem ipsum dolor sit lorem amet, consectetur</p>
  <div class="more">READ MORE <svg width="30" height="10" viewBox="0 0 30 10" fill="none" stroke="#00A9DD" stroke-width="2"><path d="M0 5h28M23 1l5 4-5 4"/></svg></div>
</div>

<!-- services -->
<h2 class="abs sec-title" style="left:0;top:1102px;width:1200px">OUR SERVICES</h2>
<p class="abs svc-intro">Lorem ipsum dolor sit amet, consectetur adipiscing elit, sed do eius mod tempor incididunt ut labore et dolore magna aliqua. Ut enim ad minim veniam, quis nostrud exercitation ullamco laboris nisi ut aliquip.</p>

<div class="abs arrow prev" style="left:48px;top:1396px">‹</div>
<div class="abs svc" style="left:109px">
  <div class="ring"><div>
    <svg width="56" height="56" viewBox="0 0 56 56" fill="none" stroke="#fff" stroke-width="3"><rect x="8" y="6" width="28" height="38" rx="2"/><path d="M14 16h14M14 24h10M14 32h8"/><circle cx="38" cy="38" r="9"/><path d="M34 38l3 3 5-6"/></svg>
  </div></div>
  <h4>Business Planning</h4>
</div>
<div class="abs svc" style="left:385px">
  <div class="ring"><div>
    <svg width="56" height="56" viewBox="0 0 56 56" fill="#fff"><rect x="6" y="30" width="44" height="4"/><rect x="10" y="34" width="3" height="14"/><rect x="43" y="34" width="3" height="14"/><circle cx="20" cy="16" r="5"/><circle cx="38" cy="12" r="5"/><rect x="15" y="22" width="10" height="8" rx="2"/><rect x="33" y="18" width="10" height="12" rx="2"/><rect x="22" y="6" width="8" height="6"/></svg>
  </div></div>
  <h4>Project Management</h4>
</div>
<div class="abs svc" style="left:637px">
  <div class="ring"><div>
    <svg width="56" height="56" viewBox="0 0 56 56" fill="#fff"><path d="M28 6c-10 0-16 8-16 18v8h32v-8c0-10-6-18-16-18z"/><rect x="14" y="34" width="28" height="12" rx="2"/><rect x="8" y="46" width="40" height="3" rx="1"/><circle cx="28" cy="40" r="2" fill="#00A9DD"/></svg>
  </div></div>
  <h4>Cyber Security</h4>
</div>
<div class="abs svc" style="left:863px">
  <div class="ring"><div>
    <svg width="56" height="56" viewBox="0 0 56 56" fill="none" stroke="#fff" stroke-width="3"><rect x="6" y="8" width="40" height="32" rx="2"/><path d="M6 15h40"/><rect x="11" y="20" width="12" height="9"/><rect x="36" y="26" width="14" height="22" rx="2"/><path d="M11 34h8M21 34h8"/></svg>
  </div></div>
  <h4>UI/UX Design</h4>
</div>
<div class="abs arrow next" style="left:1127px;top:1396px">›</div>

<!-- about -->
<div class="abs about-photo" role="img" aria-label="Photo of two consultants in discussion at a meeting table"></div>
<h2 class="abs about-title">ABOUT US</h2>
<p class="abs about-copy">Lorem ipsum dolor sit amet, consectetur adipiscing elit, sed do eius mod tempor incididunt ut labore et dolore magna aliqua. Ut enim ad minim veniam, quis nostrud exercitation ullamco laboris nisi ut aliquip ex ea commodo consequat. Lorem ipsum dolor sit amet, con sectetur adipiscing elit. Sed ut est sed nulla viverra fringilla.</p>
<div class="abs btn-dark about-btn">READ MORE
  <svg width="30" height="10" viewBox="0 0 30 10" fill="none" stroke="#fff" stroke-width="2"><path d="M0 5h28M23 1l5 4-5 4"/></svg>
</div>

<!-- testimonials -->
<h2 class="abs sec-title" style="left:0;top:2259px;width:1240px">CLIENT TESTIMONIALS</h2>
<div class="abs arrow prev" style="left:77px;top:2480px">‹</div>
<div class="abs quote-mark">“</div>
<p class="abs testi-copy">Lorem ipsum dolor sit amet, conse ctetuer adipiscing elit. Aenean comodo ligula eget dolor. Aenean massa. Cum sociis na toque pen atibus et magnis dis parturient montes, nascetur ridiculus mus. Donec quam felis, ultricies nec, pellentesque eu, pretium quis, sem. Nulla consequat massa quis enim. Donec pede justo, fringilla vel, aliquet nec, vulputate eget, arcu. In enim justo, rhoncus ut, imperdiet a, venenatis vitae, justo. Nullam dictum felis eu pede mollis pretium. Integer tincidunt. Cras dapibus. Vivamus elementum</p>
<div class="abs arrow next" style="left:1097px;top:2480px">›</div>
<div class="abs avatar" role="img" aria-label="Portrait photo of the client"></div>
<div class="abs person"><strong>Daniel Harlow</strong><span>Managing Director</span></div>
<div class="abs dots"><i class="on"></i><i></i><i></i><i></i></div>

<!-- footer -->
<footer class="abs footer"></footer>
<div class="abs newsletter">
  <h2>Our Newsletter Sign Up</h2>
  <div class="field">Enter Email Address<b>SIGNUP</b></div>
</div>

<div class="abs f-title" style="left:136px;top:2975px"><i></i>QUICK LINKS</div>
<ul class="abs links">
  <li>Home</li><li>Services</li><li>About Us</li><li>Testimonials</li><li>Contact Us</li>
</ul>

<div class="brand" style="left:390px;top:3022px;font-size:40px;color:#fff">
  <i style="width:40px;height:40px"></i>BRIDGEMONT
</div>
<span class="abs social" style="left:492px"></span>
<span class="abs social" style="left:524px"></span>
<span class="abs social" style="left:556px"></span>
<span class="abs social" style="left:588px"></span>

<div class="abs f-title" style="left:866px;top:2975px"><i></i>CONTACT US</div>
<div class="abs contact-item" style="top:3024px">
  <span class="ic"><svg width="12" height="12" viewBox="0 0 24 24" fill="none" stroke="#fff" stroke-width="2.5"><path d="M5 3h4l2 5-3 2a12 12 0 0 0 6 6l2-3 5 2v4a2 2 0 0 1-2 2A18 18 0 0 1 3 5a2 2 0 0 1 2-2z"/></svg></span>
  <span>CALL US<br>555 010 4827</span>
</div>
<div class="abs contact-item" style="top:3074px">
  <span class="ic"><svg width="12" height="10" viewBox="0 0 24 18" fill="none" stroke="#fff" stroke-width="2.5"><rect x="1" y="1" width="22" height="16" rx="2"/><path d="M1 2l11 8 11-8"/></svg></span>
  <span>EMAIL US<br>info@bridgemontgrp.com</span>
</div>
<div class="abs contact-item" style="top:3124px">
  <span class="ic"><svg width="10" height="13" viewBox="0 0 20 26" fill="#fff"><path d="M10 0a10 10 0 0 0-10 10c0 7 10 16 10 16s10-9 10-16A10 10 0 0 0 10 0zm0 14a4 4 0 1 1 0-8 4 4 0 0 1 0 8z"/></svg></span>
  <span>Address line here dummy<br>Address line here</span>
</div>

<div class="abs footer-bottom">Copyright ©2024 – All Rights Reserved by Company name</div>

</body>
</html>
```